Business card for law firm

Need business card for new law firm. Think confident, authoritative, conservative, but not stuffy or old-fashioned.

Contact Information for Business Card

Content for card - logo (uploaded), plus the following:

Paul Wexbury (larger font)
Managing Partner (larger font, but not as large as name)
Level 9, 41 Tansy Lane
Sydney NSW 2000
Main Tel 02 7346 2190
Direct Tel 02 6273 4415
Email paul@qvlegal.com.au
www.qvlegal.com.au

Letterhead design should include logo plus:
Level 9, 41 Tansy Lane
Sydney NSW 2000
Tel 02 6273 4415
www.qvlegal.com.au

```html
<!DOCTYPE html>
<html lang="en">
<head>
<meta charset="utf-8">
<title>Quayvale Legal – Business Card</title>
<link rel="stylesheet" href="https://fonts.googleapis.com/css2?family=Cinzel:wght@500;700&family=Raleway:wght@500;600&display=swap">
<style>
  :root {
    --navy: #1d2770;
    --navy-deep: #141c55;
    --ink: #1a1a2e;
    --paper: #ffffff;
    --paper-shade: #eeeeee;
    --backdrop: #3a3a3d;
    --silver: #dfe1ea;
  }
  * { box-sizing: border-box; margin: 0; padding: 0; }
  html, body {
    width: 1200px; height: 900px; overflow: hidden;
    background: var(--backdrop);
  }
  .canvas {
    position: relative; width: 1200px; height: 900px;
    display: flex; flex-direction: column; align-items: center; justify-content: center; gap: 48px;
  }
  .card {
    width: 640px; height: 366px; position: relative;
    box-shadow: 0 10px 30px rgba(0,0,0,0.45);
  }
  /* Front */
  .card-front {
    background: radial-gradient(circle at 30% 40%, var(--paper) 0%, var(--paper) 55%, var(--paper-shade) 100%);
    display: flex; align-items: center;
  }
  .brand {
    width: 300px; display: flex; flex-direction: column; align-items: center; gap: 14px;
  }
  .brand-mark { width: 34px; height: 34px; background: var(--navy); }
  .brand-name {
    font-family: "Cinzel", serif; font-weight: 500; color: var(--ink);
    font-size: 30px; letter-spacing: 1px; line-height: 1.15; text-align: center;
  }
  .divider { width: 1.5px; height: 190px; background: var(--navy); }
  .details { padding-left: 26px; color: var(--navy); font-family: "Raleway", sans-serif; }
  .person-name {
    font-family: "Cinzel", serif; font-weight: 700; font-size: 24px; letter-spacing: 0.5px; line-height: 1.1;
  }
  .person-role { font-size: 16px; font-weight: 500; margin-bottom: 12px; }
  .address { font-size: 16px; font-weight: 600; line-height: 1.3; margin-bottom: 10px; }
  .contact-list { list-style: none; font-size: 15px; font-weight: 600; line-height: 1.45; }
  .contact-list li { display: flex; align-items: center; gap: 8px; }
  .contact-list svg { width: 13px; height: 13px; fill: none; stroke: var(--navy); stroke-width: 1.6; flex: none; }
  /* Back */
  .card-back {
    background: radial-gradient(circle at 50% 30%, var(--navy) 0%, var(--navy-deep) 100%);
    display: flex; flex-direction: column; align-items: center; justify-content: center; gap: 22px;
  }
  .card-back .brand-mark { background: var(--silver); width: 44px; height: 44px; }
  .card-back .brand-name { color: var(--silver); font-size: 44px; }
  .back-web {
    font-family: "Raleway", sans-serif; font-weight: 500; color: var(--silver);
    font-size: 17px; letter-spacing: 3px;
  }
</style>
</head>
<body>
<main class="canvas">
  <section class="card card-front">
    <div class="brand">
      <span class="brand-mark"></span>
      <span class="brand-name">QUAYVALE<br>LEGAL</span>
    </div>
    <span class="divider"></span>
    <div class="details">
      <p class="person-name">PAUL WEXBURY</p>
      <p class="person-role">Managing Partner</p>
      <p class="address">Level 9, 41 Tansy Lane<br>Sydney NSW 2000</p>
      <ul class="contact-list">
        <li><svg viewBox="0 0 14 14"><path d="M3 1.5l2 2.5-1 1.5c.8 1.8 2 3 3.5 3.5l1.5-1 2.5 2-1.2 2C6 11.5 2.5 8 1.5 3.2z"/></svg>02 7346 2190</li>
        <li><svg viewBox="0 0 14 14"><rect x="3.5" y="1" width="7" height="12" rx="1"/><line x1="6" y1="11" x2="8" y2="11"/></svg>02 6273 4415</li>
        <li><svg viewBox="0 0 14 14"><rect x="1" y="3" width="12" height="8"/><path d="M1 3l6 5 6-5"/></svg>paul@qvlegal.com.au</li>
        <li><svg viewBox="0 0 14 14"><circle cx="7" cy="7" r="6"/><ellipse cx="7" cy="7" rx="2.6" ry="6"/><line x1="1" y1="7" x2="13" y2="7"/></svg>www.qvlegal.com.au</li>
      </ul>
    </div>
  </section>
  <section class="card card-back">
    <span class="brand-mark"></span>
    <span class="brand-name">QUAYVALE LEGAL</span>
    <span class="back-web">www.qvlegal.com.au</span>
  </section>
</main>
</body>
</html>
```